Flyer for The Quiet Meadow Renewal Ring

I am launching my new offering in my business at an event next Sunday where I have a booth and need a flyer advertising the offering, so the flyer needs to stand out for other practitioners that will also be there on the day offering there services.
This flyer is also what I will use for marketing on social media as well as on the day of the event. See the link below to the offering
http://carolinebirchwood.com.au/quiet-meadow-renewal-ring/

Target Market(s)

Women with body image issues - age range 25 - 65
Women with issues around food such as binge eating, emotional eating, eating disorders.

Industry/Entity Type

Health And Wellness

Font styles to use
Serif
Sans Serif
Script

Colors
f9d9e8
85cae6
cee9f5
fee18a
ffffff
eea4c8

Requirements
Must have
• Colours matching my overall website at carolinebirchwood.com.au - pinks, light blue, gold, white
• Imagery similiar to my Instagram, see below https://www.instagram.com/lanternfieldcarexq/
• - soft, warm, welcoming, nurturing, safe, inviting - see image on sales page for inspiration
• contact details
Should not have
• harsh dark colours or harsh lines

```html
<!DOCTYPE html>
<html lang="en">
<head>
<meta charset="utf-8">
<title>The Quiet Meadow Renewal Ring – Flyer</title>
<link href="https://fonts.googleapis.com/css2?family=Lato:ital,wght@0,400;0,700;0,900;1,400;1,700&display=swap" rel="stylesheet">
<style>
  :root {
    --frame: #58585a;
    --pink: #eea4c8;
    --pink-soft: #f9d9e8;
    --sky: #cee9f5;
    --sea: #85cae6;
    --ink: #1f1f22;
    --paper: #ffffff;
  }
  html, body {
    margin: 0;
    padding: 0;
    width: 919px;
    height: 1200px;
    overflow: hidden;
    background: var(--frame);
  }
  .canvas {
    position: relative;
    width: 919px;
    height: 1200px;
    background: var(--frame);
    font-family: "Lato", Arial, sans-serif;
    color: var(--ink);
  }
  .flyer {
    position: absolute;
    left: 35px;
    top: 50px;
    width: 849px;
    height: 1098px;
    overflow: hidden;
  }
  .hero-photo {
    position: absolute;
    inset: 0;
    background:
      radial-gradient(ellipse 120px 420px at 48% 45%, rgba(214,190,185,0.45), rgba(214,190,185,0) 70%),
      linear-gradient(180deg,
        #fbf7f8 0%,
        #f6eef3 22%,
        #eef2f6 40%,
        #dde8f0 52%,
        #c9dce8 64%,
        #b7cfdf 78%,
        #cfc9c6 90%,
        #d8cfc8 100%);
  }
  .wash {
    position: absolute;
    inset: 0;
    background: rgba(255,255,255,0.35);
  }
  .title {
    position: absolute;
    left: 0;
    right: 0;
    top: 53px;
    margin: 0;
    text-align: center;
    color: var(--pink);
    font-weight: 700;
    font-size: 40px;
    line-height: 50px;
  }
  .intro {
    position: absolute;
    left: 0;
    right: 0;
    top: 188px;
    margin: 0;
    text-align: center;
    font-size: 14.6px;
    line-height: 22px;
  }
  .body-copy {
    position: absolute;
    left: 110px;
    width: 630px;
    top: 452px;
    font-size: 14.4px;
    line-height: 18.6px;
    letter-spacing: -0.35px;
    white-space: nowrap;
  }
  .body-copy p { margin: 0 0 18.6px; }
  .benefits {
    list-style: none;
    margin: 0 0 18.6px;
    padding: 0 0 0 51px;
  }
  .benefits li { position: relative; }
  .benefits li::before {
    content: "";
    position: absolute;
    left: -25px;
    top: 5px;
    width: 8px;
    height: 8px;
    background: var(--pink);
  }
  .contact {
    position: absolute;
    left: 0;
    right: 0;
    top: 968px;
    text-align: center;
  }
  .contact-phone {
    margin: 0;
    font-size: 38px;
    line-height: 44px;
    font-weight: 700;
  }
  .contact-email {
    margin: 2px 0 0;
    font-size: 19px;
    font-weight: 700;
  }
</style>
</head>
<body>
<div class="canvas">
  <main class="flyer">
    <div class="hero-photo" role="img" aria-label="Soft-focus photo of a woman stretching her arms upward on a wooden jetty by a calm, misty sea"></div>
    <div class="wash"></div>

    <h1 class="title">The Quiet Meadow<br>Renewal Ring</h1>

    <p class="intro">
      It's time to make a commitment….<br>
      It's time for <b>YOU</b>, to <b>SHOW UP</b> for <b>YOU</b>…..<br>
      It's time to truly let go…….and finally heal, and find the peace that you so long for…<br>
      You deserve to feel the freedom that comes with truly loving and accepting your body.<br>
      You deserve the freedom that comes with experiencing a deeper trusting<br>
      connection with your body, where you feel safe, at home.<br>
      Can you even imagine a whole day that you didn't hate your body,<br>
      you didn't fight with food, and you felt peaceful and at home with your body?<br>
      <i>Can you love the part of you, that hates your body?</i><br>
      <i>You can't heal something you hate.</i>
    </p>

    <section class="body-copy">
      <p>It's time to show up for <b>YOU</b>, consistently, every week, and do the work, once and for all.<br>
      No more games, no more half in on <b>YOU</b>….<br>
      You deserve better than a life contained in the mental prison of body hatred.</p>

      <p>Are you truly ready to make the commitment?<br>
      How would it feel to be able to say, <b><i>“I am free to love and accept my body”</i></b>,&nbsp; and <b><i>“I am free,</i></b><br>
      <b><i>connected and at peace to my body”</i>?</b></p>

      <p>I am inviting 10 women only into this six-week healing experience, as I personally know,<br>
      that when we share our stories, it opens our hearts for other people to share their stories.<br>
      It gives us the sense we are not alone in our journey's.</p>

      <p style="margin-bottom:0">The women that come on this six-week journey will receive;</p>
      <ul class="benefits">
        <li>One 90mins one on one coaching session with me (<i>which for the women that have</i><br>
        <i>attended the Friday circle previously, can be done before this healing circle begins</i>);</li>
        <li>Private Kinfold Group to continue support outside of the circle</li>
        <li>Homework outside of circle to support your healing</li>
        <li>Journal and other small gifts weekly</li>
      </ul>

      <p>The financial investment in <b>YOU</b>, is $XX for the six weeks. For the women that have<br>
      attended the Friday night, <b>Gentle Bloom Sister Circle</b>, you will receive a discount of<br>
      $100, taking the price to $XX.<br>
      <b>Are you ready?</b></p>
    </section>

    <footer class="contact">
      <p class="contact-phone">Mobile – 0400 555 217</p>
      <p class="contact-email">Email – caroline@carolinebirchwood.com.au</p>
    </footer>
  </main>
</div>
</body>
</html>
```